Menu Design for Indian Restaurant

We are a new Indian restaurant, named Saffron Lantern Restaurant, looking for a sophisticated looking menu. It is a semi-formal dining restaurant with wooden tables and chairs and will have a focus on a creating a lively atmosphere. Environment-friendly products will be used, and the menu will be 100% vegetarian. There will be an emphasis on fresh, healthy and delicious food. We will be targeting vegans, vegetarians, health conscious people, people from all age groups, Indians, Australian's as well as other ethnic communities. We need a clean, simple, sophisticated design for the new restaurant menu. Attached is the restaurant logo for reference.

UPDATE:
- We have attached the menu
- We are not looking for any particular type of layout or size (open to suggests). Please suggest this after having a look at the menu contents. However, we will be having one formal menu to be used in the restaurant, and one in brochure form for distribution.
- There are no images at present. If you feel the need of images, please use sample images for now.

Thank you for the entries thus far.
Updates

Target Market(s)

All age groups from different nationalities

Industry/Entity Type

Indian Restaurant

Colors

Designer to choose colors to be used in the design.

Requirements
Nice to have
• This will be printed on environmentally friendly paper.

```html
<!DOCTYPE html>
<html lang="en">
<head>
<meta charset="utf-8">
<title>Saffron Lantern Restaurant – Breakfast Menu</title>
<link href="https://fonts.googleapis.com/css2?family=Alegreya+Sans:ital,wght@0,400;0,500;0,700;1,700&family=Roboto:ital,wght@0,700;1,900&display=swap" rel="stylesheet">
<style>
:root{
  --saffron:#f58634;
  --saffron-soft:#f8a56d;
  --green:#15a35a;
  --green-soft:#6fcf9b;
  --ink:#231f20;
  --desc:#e07a2c;
  --dark:#2b2b2b;
  --paper:#ffffff;
  --frame-grey:#8a8a8a;
}
*{margin:0;padding:0;box-sizing:border-box}
html,body{width:1200px;height:1158px;overflow:hidden;background:var(--paper)}
body{position:relative;font-family:"Alegreya Sans",sans-serif;color:var(--ink)}
.page{position:absolute;top:0;width:582px;height:1119px;border:1px solid var(--frame-grey);overflow:hidden;
  background:linear-gradient(180deg,var(--saffron-soft) 0%,#fbc8a3 14%,#fde6d5 24%,#fff 31%,#fff 78%,#c9ecd8 90%,var(--green-soft) 100%)}
.page--two{left:0}
.page--three{left:618px}
.page-art{position:absolute;inset:0;width:100%;height:100%}
.section-tab{position:absolute;left:58px;top:394px;width:286px;height:30px}
.section-tab__title{position:absolute;left:33px;top:1px;font-family:"Roboto",sans-serif;font-style:italic;font-weight:900;font-size:21px;color:#fff;letter-spacing:.3px}
.section-note{position:absolute;left:58px;top:429px;font-weight:700;font-style:italic;font-size:14.5px;line-height:18.4px;color:var(--desc)}
.item{position:absolute;left:58px;right:56px}
.item__name{font-size:17.5px;font-weight:500;line-height:22px;display:block}
.item__extra{font-size:13px;font-weight:500}
.item__price{position:absolute;right:0;top:1px;font-size:17px;font-weight:500;line-height:22px;font-variant-numeric:oldstyle-nums}
.item__desc{display:block;margin-top:0;font-size:13.6px;font-weight:500;line-height:18.6px;color:var(--desc);max-width:402px}
.page-label{position:absolute;top:1130px;font-family:"Roboto",sans-serif;font-weight:700;font-size:29px;color:var(--dark);width:200px;text-align:center}
</style>
</head>
<body>

<section class="page page--two">
  <svg class="page-art" viewBox="0 0 727 1398" preserveAspectRatio="none">
    <rect x="0" y="0" width="727" height="340" fill="#f79a5c" opacity=".2" role="img" aria-label="Floral lace pattern in saffron tones"/>
    <path d="M38,480 C38,470 72,455 70,425 C68,395 30,390 25,370 C20,260 110,205 225,190 C215,130 290,95 363,78 C436,95 511,130 501,190 C616,205 706,260 701,370 C696,390 658,395 656,425 C654,455 688,470 688,480 L688,1358 L38,1358 Z" fill="#fff"/>
    <path d="M38,480 C38,470 72,455 70,425 C68,395 30,390 25,370 C20,260 110,205 225,190 C215,130 290,95 363,78 C436,95 511,130 501,190 C616,205 706,260 701,370 C696,390 658,395 656,425 C654,455 688,470 688,480" fill="none" stroke="#f58634" stroke-width="5"/>
    <g fill="none" stroke-width="5">
      <line x1="38" y1="478" x2="38" y2="866" stroke="#f58634"/>
      <line x1="38" y1="893" x2="38" y2="1358" stroke="#15a35a"/>
      <line x1="688" y1="478" x2="688" y2="676" stroke="#f58634"/>
      <line x1="688" y1="703" x2="688" y2="1358" stroke="#15a35a"/>
      <line x1="36" y1="1358" x2="690" y2="1358" stroke="#15a35a"/>
    </g>
    <rect x="208" y="252" width="312" height="70" rx="30" fill="#f7953a" role="img" aria-label="Saffron brush stroke"/>
    <rect x="208" y="368" width="312" height="70" rx="30" fill="#168a45" role="img" aria-label="Green brush stroke"/>
    <polygon points="73,493 408,493 428,512 408,530 73,530" fill="#f58634"/>
    <polygon points="73,493 93,512 73,530" fill="#2b2b2b"/>
    <polygon points="408,493 428,512 408,530" fill="#2b2b2b"/>
  </svg>
  <div class="section-tab"><span class="section-tab__title">BREAKFAST</span></div>
  <p class="section-note">Dosa/ Vada/ Idli served with sambar (Lentil),<br>coconut chutney and tomato chilli chutney</p>

  <div class="item" style="top:476px"><span class="item__name">Rava Dosa</span><span class="item__price">9.9</span><span class="item__desc">Crispy crepe made with ground rice and lentils gluten free</span></div>
  <div class="item" style="top:523px"><span class="item__name">Kanda Rava Dosa</span><span class="item__price">11.9</span><span class="item__desc">Crispy crepe made with ground rice and lentil and onion stuffed with<br>potatoes</span></div>
  <div class="item" style="top:589px"><span class="item__name">Masala Rava Dosa</span><span class="item__price">11.9</span><span class="item__desc">Crispy crepe made with ground rice and lentil stuffed with potatoes</span></div>
  <div class="item" style="top:636px"><span class="item__name">Plain Dosa</span><span class="item__price">9.9</span><span class="item__desc">Crispy crepe made with rice and lentil batter with clarified butter</span></div>
  <div class="item" style="top:683px"><span class="item__name">Masala Dosa</span><span class="item__price">11.9</span><span class="item__desc">Crispy crepe made with rice and lentil batter stuffed with potatoes</span></div>
  <div class="item" style="top:731px"><span class="item__name">Vada Sambar</span><span class="item__price">7.9</span><span class="item__desc">Lentil dumpling deep fry</span></div>
  <div class="item" style="top:778px"><span class="item__name">Thair Bara</span><span class="item__price">7.9</span><span class="item__desc">Lentil dumpling deep fry in yogurt buttermilk</span></div>
  <div class="item" style="top:825px"><span class="item__name">Idly</span><span class="item__price">7.9</span><span class="item__desc">Dumpling made with black lentil rice steamed fermented</span></div>
  <div class="item" style="top:872px"><span class="item__name">Sev Batata Puri (6)</span><span class="item__price">5.9</span><span class="item__desc">Fried puff balls fills with potatoes onion yogurt date and mint chutney<br>fine gram crunchy noodle made with gram flour</span></div>
  <div class="item" style="top:938px"><span class="item__name">Bhel Puri</span><span class="item__price">6.9</span><span class="item__desc">Rice puff fresh green chilli red onion tomatoes fresh coriander</span></div>
  <div class="item" style="top:985px"><span class="item__name">Batata Pao (2pcs)</span><span class="item__price">7.9</span></div>
  <div class="item" style="top:1014px"><span class="item__name">Puri Bhaji (4pcs)</span><span class="item__price">7.9</span></div>
  <div class="item" style="top:1042px"><span class="item__name">Pao Bhaji (2pcs)</span><span class="item__price">7.9</span></div>
</section>

<section class="page page--three">
  <svg class="page-art" viewBox="0 0 727 1398" preserveAspectRatio="none">
    <rect x="0" y="0" width="727" height="340" fill="#f79a5c" opacity=".2" role="img" aria-label="Floral lace pattern in saffron tones"/>
    <path d="M38,480 C38,470 72,455 70,425 C68,395 30,390 25,370 C20,260 110,205 225,190 C215,130 290,95 363,78 C436,95 511,130 501,190 C616,205 706,260 701,370 C696,390 658,395 656,425 C654,455 688,470 688,480 L688,1358 L38,1358 Z" fill="#fff"/>
    <path d="M38,480 C38,470 72,455 70,425 C68,395 30,390 25,370 C20,260 110,205 225,190 C215,130 290,95 363,78 C436,95 511,130 501,190 C616,205 706,260 701,370 C696,390 658,395 656,425 C654,455 688,470 688,480" fill="none" stroke="#f58634" stroke-width="5"/>
    <g fill="none" stroke-width="5">
      <line x1="38" y1="478" x2="38" y2="866" stroke="#f58634"/>
      <line x1="38" y1="893" x2="38" y2="1358" stroke="#15a35a"/>
      <line x1="688" y1="478" x2="688" y2="676" stroke="#f58634"/>
      <line x1="688" y1="703" x2="688" y2="1358" stroke="#15a35a"/>
      <line x1="36" y1="1358" x2="690" y2="1358" stroke="#15a35a"/>
    </g>
    <rect x="208" y="252" width="312" height="70" rx="30" fill="#f7953a" role="img" aria-label="Saffron brush stroke"/>
    <rect x="208" y="368" width="312" height="70" rx="30" fill="#168a45" role="img" aria-label="Green brush stroke"/>
    <polygon points="73,493 408,493 428,512 408,530 73,530" fill="#f58634"/>
    <polygon points="73,493 93,512 73,530" fill="#2b2b2b"/>
    <polygon points="408,493 428,512 408,530" fill="#2b2b2b"/>
  </svg>
  <div class="section-tab"><span class="section-tab__title">BREAKFAST</span></div>
  <p class="section-note">Dosa/ Vada/ Idli served with sambar (Lentil),<br>coconut chutney and tomato chilli chutney</p>

  <div class="item" style="top:476px"><span class="item__name">Aloo Parantha (2pcs)</span><span class="item__price">7.9</span><span class="item__desc">with yogurt, pickle</span></div>
  <div class="item" style="top:521px"><span class="item__name">Gobhi Parantha (2pcs)</span><span class="item__price">7.9</span><span class="item__desc">with yogurt, pickle</span></div>
  <div class="item" style="top:566px"><span class="item__name">Muli Parantha (2pcs)</span><span class="item__price">7.9</span><span class="item__desc">with yogurt, pickle</span></div>
  <div class="item" style="top:611px"><span class="item__name">Thepla (4pcs)</span><span class="item__price">7.9</span><span class="item__desc">with yogurt, pickle</span></div>
  <div class="item" style="top:655px"><span class="item__name">Vati Khaman Dhokla (4pcs)</span><span class="item__price">6.9</span><span class="item__desc">Fluffy soft cake soak and crushed lentil</span></div>
  <div class="item" style="top:700px"><span class="item__name">Kachori Aloo Sabji</span><span class="item__price">7.9</span><span class="item__desc">Stuffed legume with potato curry</span></div>
  <div class="item" style="top:745px"><span class="item__name">Bhature Chole (2pcs)</span><span class="item__price">9.9</span><span class="item__desc">Chickpeas, pickle , salad, fried bread</span></div>
  <div class="item" style="top:789px"><span class="item__name">Uttapam (2pc) <span class="item__extra">with sambar, chutney</span></span><span class="item__price">7.9</span><span class="item__desc">Tomato onion chilli coriander</span></div>
  <div class="item" style="top:834px"><span class="item__name">Dhai Jalebi with yogurt</span><span class="item__price">4.9</span></div>
  <div class="item" style="top:861px"><span class="item__name">Zesto Noodles</span><span class="item__price">7.9</span><span class="item__desc">Topped with chopped cucumbers tomato onion</span></div>
  <div class="item" style="top:906px"><span class="item__name">Muesli Yogurt Fruit</span><span class="item__price">5.9</span></div>
  <div class="item" style="top:933px"><span class="item__name">Oats</span><span class="item__price">5.9</span><span class="item__desc">Warm milk banana</span></div>
  <div class="item" style="top:978px"><span class="item__name">Waffle</span><span class="item__price">6.9</span><span class="item__desc">Cream chocolate fruit</span></div>
  <div class="item" style="top:1023px"><span class="item__name">Vegetarian Sandwich</span><span class="item__price">5.9</span><span class="item__desc">Cucumber tomato cheese</span></div>
</section>

<div class="page-label" style="left:191px">PAGE 2</div>
<div class="page-label" style="left:809px">PAGE 3</div>

</body>
</html>
```